Pause Your Day And Browse- PYDB poster

I am the Vice President of Advocacy for the Coastline Shelfkeepers Guild. I am looking to have a set of posters made for PYDB (Pause Your Day and Browse) October 23. PYDB is a time when all school children in BC are encouraged to Pause Your Day and Browse for 15-20 minutes at some point in their day.

I would like to get a set of 2 digital posters designed (if possible it would be nice to have the option to print to both 11 x 17 and 8.5 x 11 paper). We need a poster that is high school (Grade 8-12) appropriate and one that is elementary (Grade k-7) appropriate. Both posters need to be replicated in French. All posters need to have the KWNU logo on them as well as the Coastline Shelfkeepers Guild Logo.

Here is a link to last year's successful design http://kwnu-example.org/csg/info/advocacy.html
There are two additional samples in the uploaded files section.

Each poster needs to have the following information:

-Pause Your Day and Browse (PYDB)
- The date Monday, October 23, 2017
-the logo for the KWNU (attached)
-the logo for the CSG (attached)- the logos do not have to be large.

Target Market(s)

Children ages 5-12 and 12-17 as well as their teachers

Industry/Entity Type

Teacher

Font styles to use
Sans Serif

Requirements
Must have
• Must have both logos- colours may be changed for either or both
Nice to have
• Clear, Bright lettering. Images of child or children enjoying reading
Should not have
• stereotypes

```html
<!DOCTYPE html>
<html lang="fr">
<head>
<meta charset="utf-8">
<title>PYDB – Fais une pause et feuillette</title>
<link rel="stylesheet" href="https://fonts.googleapis.com/css2?family=Archivo+Black&family=Montserrat:ital,wght@0,600;0,800;1,700&display=swap">
<style>
  :root {
    --paper: #ffffff;
    --teal: #1b8f8f;
    --teal-deep: #116b68;
    --teal-fold: #2aa3a0;
    --ribbon: #97282c;
    --gold: #fbb44d;
    --navy: #2e327a;
    --ink-white: #ffffff;
  }
  * { margin: 0; padding: 0; box-sizing: border-box; }
  html, body {
    width: 1200px; height: 1000px; overflow: hidden;
    background: var(--paper);
  }
  .poster {
    position: relative; width: 1200px; height: 1000px;
    font-family: "Montserrat", sans-serif;
  }
  .poster__backdrop { position: absolute; inset: 0; }
  .poster__art {
    position: absolute; left: 285px; top: 165px; width: 610px; height: 218px;
    background: linear-gradient(180deg, var(--teal-deep) 0%, var(--teal-deep) 62%, #e9eaeb 62%, #d6d8da 92%, var(--teal-deep) 92%);
    border-radius: 14px 14px 8px 8px;
  }
  .poster__title {
    position: absolute; left: 0; top: 0; width: 1200px; height: 1000px;
    pointer-events: none;
  }
  .poster__title-text {
    font-family: "Archivo Black", sans-serif;
    font-size: 292px; letter-spacing: 8px;
  }
  .poster__title-shadow { fill: var(--navy); }
  .poster__title-fill { fill: var(--gold); }
  .poster__title-line {
    fill: none; stroke: var(--ink-white); stroke-width: 2.5; stroke-linejoin: round;
  }
  .poster__tagline {
    position: absolute; left: 60px; width: 1050px; top: 652px;
    text-align: center; color: var(--ink-white);
    font-style: italic; font-weight: 700; font-size: 38px; letter-spacing: 0.13em;
  }
  .poster__date {
    position: absolute; left: 420px; top: 757px; width: 372px; height: 46px;
    background: var(--paper); color: var(--teal);
    border-radius: 23px; display: flex; align-items: center; justify-content: center;
    font-weight: 600; font-size: 29px; letter-spacing: 0.08em;
  }
  .partners {
    position: absolute; right: 78px; bottom: 120px;
    display: flex; align-items: center; gap: 16px;
  }
  .partner {
    display: flex; align-items: center; gap: 6px;
    color: var(--navy); font-weight: 800; font-size: 22px;
  }
  .partner__dot {
    width: 22px; height: 22px; border-radius: 50%; background: var(--navy);
  }
</style>
</head>
<body>
<main class="poster">
  <svg class="poster__backdrop" width="1200" height="1000" viewBox="0 0 1200 1000" aria-hidden="true">
    <path class="panel" d="M60 73 H1143 V640 L815 912 H60 Z" fill="var(--teal)"/>
    <path class="panel-curl" d="M1143 640 L815 912 C930 800 1030 690 1070 525 C1095 575 1120 612 1143 640 Z" fill="var(--teal-fold)"/>
    <polygon class="ribbon" points="970,73 1063,73 1063,297 1016,255 970,297" fill="var(--ribbon)"/>
  </svg>

  <div class="poster__art" role="img" aria-label="Two children sitting on top of a large open book, each reading a book"></div>

  <h1 aria-label="PYDB">
    <svg class="poster__title" width="1200" height="1000" viewBox="0 0 1200 1000" aria-hidden="true">
      <text class="poster__title-text poster__title-shadow" x="573" y="628" text-anchor="middle">PYDB</text>
      <text class="poster__title-text poster__title-fill" x="585" y="618" text-anchor="middle">PYDB</text>
      <text class="poster__title-text poster__title-line" x="591" y="612" text-anchor="middle">PYDB</text>
    </svg>
  </h1>

  <p class="poster__tagline">FAIS UNE PAUSE ET FEUILLETTE</p>

  <p class="poster__date">OCTOBER 23, 2017</p>

  <footer class="partners">
    <span class="partner"><span class="partner__dot"></span>KWNU</span>
    <span class="partner">CSG</span>
  </footer>
</main>
</body>
</html>
```